Business Card - Existing Logo & Branding copied to Business Card Format

We are looking for a designer to help with designing a two sided business card for us. We sell a web based software platform that helps people sell access to online training.
We have an existing logo and recently completed a design project here on sketch hive to have someone design a nice trade show booth for us (also attached file for that design as well as our logo). We really like the look and feel of the tradeshow booth design. The fonts, colors, etc all work for us. We are hoping someone can create something very similar just in business card format.
Should be pretty straight forward hopefully....
On one side we want the logo, employee name, email address, phone and fax. On the other side we would like the text "transform your organizations training, revenue products = revenue" - See the attached PSD for what we want that to look like.
You can also see our website at www.tidalsparrow.com for an example of our branding.
We are open to ideas, have done several projects on sketch hive and love when designers come up with creative approaches that are even better then what we envisioned.
Software

```html
<!DOCTYPE html>
<html lang="en">
<head>
<meta charset="utf-8">
<title>TidalSparrow Business Card</title>
<link rel="stylesheet" href="https://fonts.googleapis.com/css2?family=Open+Sans:wght@400;600;700&family=Courier+Prime:wght@400;700&display=swap">
<style>
  :root {
    --brand-red: #b01c2a;
    --brand-red-dark: #7e1220;
    --brand-red-light: #c42636;
    --ink: #3c3c3e;
    --paper: #ffffff;
    --paper-shade: #f1f1f1;
    --backdrop: #e9e6e1;
    --sans: "Open Sans", Arial, sans-serif;
    --slab: "Courier Prime", "Courier New", monospace;
  }
  * { box-sizing: border-box; margin: 0; padding: 0; }
  html, body { width: 1200px; height: 900px; overflow: hidden; }
  body {
    background: var(--backdrop);
    display: flex;
    flex-direction: column;
    align-items: center;
    justify-content: center;
    gap: 48px;
  }
  .card {
    position: relative;
    width: 640px;
    height: 366px;
    overflow: hidden;
    box-shadow: 0 6px 18px rgba(0,0,0,0.18);
  }

  /* Front side */
  .card-front {
    background: radial-gradient(ellipse at 50% 30%, var(--brand-red-light) 0%, var(--brand-red) 45%, var(--brand-red-dark) 100%);
    color: var(--paper);
  }
  .front-decoration {
    position: absolute;
    inset: 0;
    background:
      radial-gradient(circle at 30% 62%, rgba(255,255,255,0.05) 0 18%, transparent 19%),
      radial-gradient(circle at 70% 28%, rgba(255,255,255,0.05) 0 22%, transparent 23%);
  }
  .tagline {
    position: absolute;
    left: 86px;
    top: 132px;
    width: 500px;
  }
  .tagline-lead {
    font-family: var(--sans);
    font-size: 18px;
    font-weight: 400;
    line-height: 1.2;
  }
  .tagline-row {
    display: flex;
    align-items: baseline;
    gap: 16px;
    margin-top: 2px;
  }
  .tagline-subjects {
    font-family: var(--slab);
    font-weight: 700;
    font-size: 16px;
    line-height: 1.2;
    letter-spacing: 1px;
  }
  .tagline-equals {
    font-family: var(--slab);
    font-weight: 700;
    font-size: 26px;
  }
  .tagline-result {
    font-family: var(--slab);
    font-weight: 700;
    font-size: 26px;
    letter-spacing: 1px;
  }
  .front-brand {
    position: absolute;
    left: 0; right: 0;
    bottom: 78px;
    display: flex;
    justify-content: center;
    align-items: center;
    gap: 8px;
  }
  .brand-square {
    width: 28px;
    height: 28px;
    background: var(--paper);
  }
  .front-brand .brand-name {
    font-family: var(--sans);
    font-weight: 600;
    font-size: 26px;
    color: var(--paper);
  }

  /* Back side */
  .card-back {
    background: linear-gradient(180deg, var(--paper) 0%, var(--paper-shade) 100%);
  }
  .back-frame {
    position: absolute;
    inset: 0;
  }
  .back-brand {
    position: absolute;
    top: 24px;
    left: 0; right: 0;
    display: flex;
    justify-content: center;
  }
  .back-brand-inner {
    display: flex;
    align-items: center;
    gap: 10px;
    padding: 0 14px;
    background: var(--paper);
  }
  .back-brand .brand-square {
    width: 42px;
    height: 42px;
    background: var(--brand-red);
  }
  .back-brand .brand-name {
    font-family: var(--sans);
    font-weight: 600;
    font-size: 36px;
    color: var(--ink);
  }
  .holder {
    position: absolute;
    top: 112px;
    left: 0; right: 0;
    text-align: center;
  }
  .holder-name {
    font-family: var(--slab);
    font-weight: 700;
    font-size: 24px;
    letter-spacing: 2px;
    color: var(--brand-red);
  }
  .holder-title {
    font-family: var(--slab);
    font-weight: 700;
    font-size: 18px;
    color: var(--ink);
    margin-top: 2px;
  }
  .contacts {
    position: absolute;
    top: 218px;
    left: 110px;
    right: 70px;
    display: flex;
    justify-content: space-between;
    font-family: var(--sans);
    font-size: 14px;
    color: var(--paper);
  }
  .contact-column { display: flex; flex-direction: column; gap: 16px; }
  .contact-item { display: flex; align-items: center; gap: 10px; }
  .contact-icon { width: 16px; height: 16px; flex: none; }
  .contact-at { font-weight: 700; font-size: 15px; width: 16px; text-align: center; }
</style>
</head>
<body>

  <section class="card card-front" aria-label="Business card front">
    <div class="front-decoration" role="img" aria-label="Faint line drawings of light bulbs"></div>
    <div class="tagline">
      <p class="tagline-lead">Turn your company's</p>
      <div class="tagline-row">
        <p class="tagline-subjects">COURSES, KNOWLEDGE<br>and SERVICES</p>
        <span class="tagline-equals">=</span>
        <p class="tagline-result">Income</p>
      </div>
    </div>
    <div class="front-brand">
      <span class="brand-square"></span>
      <span class="brand-name">TidalSparrow</span>
    </div>
  </section>

  <section class="card card-back" aria-label="Business card back">
    <svg class="back-frame" width="640" height="366" viewBox="0 0 640 366">
      <polyline points="50,48 50,205" fill="none" stroke="var(--brand-red)" stroke-width="2.5"/>
      <polyline points="590,205 590,48 50,48" fill="none" stroke="var(--brand-red)" stroke-width="2.5"/>
      <path d="M50,200 H590 V300 H588 L586,324 L560,300 H50 Z" fill="var(--brand-red)"/>
    </svg>

    <div class="back-brand">
      <div class="back-brand-inner">
        <span class="brand-square"></span>
        <span class="brand-name">TidalSparrow</span>
      </div>
    </div>

    <div class="holder">
      <p class="holder-name">MARCUS FELDHAVEN</p>
      <p class="holder-title">Lead Architect</p>
    </div>

    <div class="contacts">
      <div class="contact-column">
        <p class="contact-item"><span class="contact-at">@</span>alex.morgan@tidalsparrow.com</p>
        <p class="contact-item">
          <svg class="contact-icon" viewBox="0 0 16 16"><path d="M4 2 L4 14 L7 11 L9 15 L11 14 L9 10 L13 10 Z" fill="var(--paper)"/></svg>
          www.TidalSparrow.com
        </p>
      </div>
      <div class="contact-column">
        <p class="contact-item">
          <svg class="contact-icon" viewBox="0 0 16 16"><path d="M3 2 L6 2 L7 5 L5.5 6.5 Q7 9.5 9.5 10.5 L11 9 L14 10 L14 13 Q13 14.5 11 14 Q4 12 2 5 Q1.5 3 3 2 Z" fill="var(--paper)"/></svg>
          (800) 555 0142
        </p>
        <p class="contact-item">
          <svg class="contact-icon" viewBox="0 0 16 16"><rect x="4" y="1" width="8" height="14" rx="1.5" fill="var(--paper)"/><rect x="5.5" y="3" width="5" height="8" fill="var(--brand-red)"/></svg>
          (425) 555 0187
        </p>
      </div>
    </div>
  </section>

</body>
</html>
```